Either a trifold or double sided flyer/brochure

A flyer to help spark interest in a historic preservation project in Alder Falls, NH--looking for something that captures the early 19th century rural village and mill times--American Primitive, Shaker, Cross Stitch Sampler...must be able to highlight home history as well as have all owners of house on a single page. Word document attached--can also provide files for the house painting, color photos, dunby photo, advertising photo or part of original settler map.
I like this brochure
http://tovabrenick.com/wordpress/pell-barn-museum-brochure/
community stakeholders, residents,
Historic Preservation, House Museums.

```html
<!DOCTYPE html>
<html lang="en">
<head>
<meta charset="utf-8">
<title>The Hartwell Homestead History c. 1826 – Trifold Brochure</title>
<link href="https://fonts.googleapis.com/css2?family=PT+Sans+Narrow:wght@400;700&family=Open+Sans:wght@600;800&display=swap" rel="stylesheet">
<style>
:root{
  --page:#ececec;
  --brown-dark:#3a2a1e;
  --brown-mid:#5e4636;
  --brown-light:#7a604d;
  --navy:#1f3461;
  --navy-deep:#233763;
  --stripe:#2d4270;
  --blue-mid:#3a5ea8;
  --blue-light:#a7b6d1;
  --blue-pale:#b4c2da;
  --white:#ffffff;
  --ink:#2b2b33;
}
*{box-sizing:border-box;margin:0;padding:0}
html,body{width:967px;height:1200px;overflow:hidden;background:var(--page)}
body{position:relative;font-family:"PT Sans Narrow",sans-serif}
.spread{position:absolute;left:113px;width:740px;height:574px;background:var(--white);overflow:hidden}
.spread--outside{top:14px}
.spread--inside{top:612px}
.block{position:absolute}
.band-top{top:0;height:19px}
.band-bottom{top:557px;height:17px}

/* outside spread */
.owners{left:0;top:23px;width:272px;height:530px;background:linear-gradient(90deg,var(--brown-dark),var(--brown-mid) 70%,var(--brown-light));color:var(--white)}
.owners__title{font-family:"Open Sans",sans-serif;font-weight:600;font-size:13.6px;line-height:17px;text-align:center;letter-spacing:.4px;margin-top:11px}
.owner-list{position:absolute;left:19px;right:19px;font-size:9px;line-height:13px}
.owner-list--upper{top:68px}
.owner-list--lower{top:375px;left:23px}
.owner{display:flex;align-items:baseline;white-space:nowrap}
.owner__name{flex:0 0 auto}
.owner__dots{flex:1 1 auto;border-bottom:1px dotted rgba(255,255,255,.8);margin:0 3px;transform:translateY(-2px)}
.owner__years{flex:0 0 auto}
.owner-note{font-size:9px;line-height:13px}
.gap{height:13px}
.owners__photo{position:absolute;left:61px;top:202px;width:150px;height:151px;border:3px solid var(--white);border-radius:3px;background:linear-gradient(160deg,#b9b4ac,#5f5a54)}

.painting{left:280px;top:22px;width:433px;height:249px;background:linear-gradient(180deg,#a8bfd6 0%,#7d9cb9 35%,#3f5d86 55%,#4b5f3e 80%,#3a4a2f 100%)}
.outer-stripe{left:713px;top:23px;width:27px;height:530px;background:var(--stripe)}
.invite{left:280px;top:271px;width:212px;height:282px;background:linear-gradient(180deg,var(--blue-mid),#2f4f96)}
.invite__text{position:absolute;left:8px;right:6px;top:10px;color:var(--white);font-size:9.6px;line-height:20px;text-align:center}
.invite__text .line{font-size:10.6px}
.invite__dot{display:inline-block;width:13px;height:13px;border:1.5px solid var(--white);border-radius:50%;vertical-align:-3px;margin-right:3px}
.house-photo{left:280px;top:350px;width:212px;height:203px;background:linear-gradient(160deg,#5a7ccc,#2c4f9e 60%,#4a5c7e)}
.cover{left:492px;top:271px;width:221px;height:282px;background:var(--blue-light)}
.cover__title{position:absolute;left:504px;top:225px;width:171px;height:151px;background:var(--navy);border:3px solid var(--white);border-radius:3px;color:var(--white);font-family:"Open Sans",sans-serif;font-weight:800;padding:10px 0 0 15px}
.cover__title .big{font-size:19px;line-height:20.5px;letter-spacing:.3px}
.cover__title .year{font-size:23px;line-height:24px}
.cover__title .place{font-size:14px;line-height:16.5px;margin-top:2px}
.map{left:507px;top:380px;width:190px;height:173px;background:linear-gradient(135deg,#d7dde8,#b7c3d6)}

/* inside spread */
.portrait{left:0;top:22px;width:260px;height:531px;background:linear-gradient(160deg,#6e5b48,#8f7a63 40%,#6a5642 75%,#4e3f31)}
.portrait-edge{left:260px;top:22px;width:12px;height:531px;background:var(--brown-mid)}
.history-title{position:absolute;left:23px;top:88px;color:var(--white);font-family:"Open Sans",sans-serif;font-weight:800}
.history-title .big{font-size:15.5px;line-height:15.4px;letter-spacing:.3px}
.history-title .place{font-size:11.5px;line-height:13px}
.story{position:absolute;color:var(--white);font-size:10.6px;line-height:14.3px}
.story p+p{margin-top:8px}
.story--left{left:26px;top:190px;width:208px;text-shadow:0 0 2px rgba(0,0,0,.4)}
.story--middle{left:286px;top:30px;width:202px}
.story-box{left:280px;top:22px;width:212px;height:261px;background:linear-gradient(90deg,#6a5140,#7e6654)}
.stairs{left:280px;top:283px;width:212px;height:270px;background:linear-gradient(160deg,#7b6047,#d2cfc4 45%,#5c4330 80%)}
.autumn{left:492px;top:22px;width:220px;height:101px;background:linear-gradient(180deg,#8e6a3d,#a7884b 50%,#4d4a2e)}
.memoir{left:492px;top:126px;width:220px;height:325px;background:var(--blue-pale)}
.story--right{left:500px;top:132px;width:205px;color:var(--ink)}
.story--right p+p{margin-top:12px}
.winter{left:492px;top:455px;width:220px;height:98px;background:linear-gradient(180deg,#7f7565,#c9a63e 45%,#eef0f3)}
.inside-stripe{left:712px;top:22px;width:28px;height:531px;background:var(--brown-mid)}
</style>
</head>
<body>

<section class="spread spread--outside" aria-label="Brochure outside">
  <div class="block band-top" style="left:0;width:272px;background:linear-gradient(90deg,var(--brown-dark),var(--brown-light))"></div>
  <div class="block band-top" style="left:280px;width:212px;background:var(--navy-deep)"></div>
  <div class="block band-top" style="left:492px;width:221px;background:var(--blue-light)"></div>
  <div class="block band-top" style="left:713px;width:27px;background:var(--stripe)"></div>
  <div class="block band-bottom" style="left:0;width:272px;background:linear-gradient(90deg,var(--brown-dark),var(--brown-light))"></div>
  <div class="block band-bottom" style="left:280px;width:212px;background:var(--navy-deep)"></div>
  <div class="block band-bottom" style="left:492px;width:221px;background:var(--blue-light)"></div>
  <div class="block band-bottom" style="left:713px;width:27px;background:var(--stripe)"></div>

  <div class="block owners">
    <h2 class="owners__title">OWNERS OF 47 ALDER LANE<br>ALDER FALLS, NEW HAMPSHIRE</h2>
    <div class="owner-list owner-list--upper">
      <div class="owner"><span class="owner__name">Robert Ashby (grandson of John Ashby) owned the land</span><span class="owner__dots"></span><span class="owner__years">1826</span></div>
      <div class="owner"><span class="owner__name">George S. Hartwell and Jane (Pruett) Hartwell</span><span class="owner__dots"></span><span class="owner__years">1826-1828</span></div>
      <div class="owner"><span class="owner__name">Deacon Thomas Larkin and Alice (Mercer) Larkin (Baptist)</span><span class="owner__years">&nbsp;1828-1839</span></div>
      <div class="owner"><span class="owner__name">Elijah Brown Thayer and Achsah (Lund) Thayer</span><span class="owner__dots"></span><span class="owner__years">1839-1877</span></div>
      <div class="owner-note">(mortgage between Samuel Mercer and Thayer is 1845)</div>
      <div class="gap"></div>
      <div class="owner"><span class="owner__name">Mary Ellen Thayer</span><span class="owner__dots"></span><span class="owner__years">1877-1898</span></div>
      <div class="gap"></div>
      <div class="owner"><span class="owner__name">James Corliss</span><span class="owner__dots"></span><span class="owner__years">1898-1904</span></div>
    </div>
    <div class="owners__photo" role="img" aria-label="Black and white photograph of an elderly couple seated in a parlour"></div>
    <div class="owner-list owner-list--lower">
      <div class="owner"><span class="owner__name">Fred Parker Dunby and Grace E. (Hollis) Dunby</span><span class="owner__dots"></span><span class="owner__years">1904-1956</span></div>
      <div class="gap"></div>
      <div class="owner"><span class="owner__name">Elinor (Dunby) Fairbrook and Frank O Fairbrook</span><span class="owner__dots"></span><span class="owner__years">1955-1998</span></div>
      <div class="owner-note">(Elinor was born in house on July 29, 1911)</div>
      <div class="gap"></div>
      <div class="owner"><span class="owner__name">James H. Wendholt and Maria Ortega Wendholt</span><span class="owner__dots"></span><span class="owner__years">1998-2015</span></div>
      <div class="owner-note">(James was nephew of Elinor (Dunby) Fairbrook)</div>
      <div class="gap"></div>
      <div class="owner"><span class="owner__name">Brookhaven</span><span class="owner__dots"></span><span class="owner__years">2015-2022</span></div>
      <div class="gap"></div>
      <div class="owner"><span class="owner__name">Edward M. Salvo and Albert A. Pennings, Jr.</span><span class="owner__dots"></span><span class="owner__years">2022</span></div>
    </div>
  </div>

  <div class="block painting" role="img" aria-label="Folk-style painting of the white farmhouse, ell and barn under a blue sky"></div>
  <div class="block outer-stripe"></div>
  <div class="block invite">
    <p class="invite__text"><span class="invite__dot"></span>They invite you to join their Townpost Group<br><span class="line">Hartwell Homestead c. 1826, Dunbys Corner,</span><br><span class="line">Alder Falls, New Hampshire</span></p>
  </div>
  <div class="block house-photo" role="img" aria-label="Photograph of the clapboard house gable with tree shadows, tinted blue"></div>
  <div class="block cover"></div>
  <h1 class="cover__title"><div class="big">The Hartwell<br>Homestead<br>History c.<br><span class="year">1826</span></div><div class="place">Alder Falls,<br>New Hampshire</div></h1>
  <div class="block map" role="img" aria-label="Section of an early settler lot map showing the river and neighbouring lots"></div>
</section>

<section class="spread spread--inside" aria-label="Brochure inside">
  <div class="block band-top" style="left:0;width:272px;background:var(--brown-mid)"></div>
  <div class="block band-top" style="left:280px;width:212px;background:linear-gradient(90deg,var(--brown-light),var(--brown-dark))"></div>
  <div class="block band-top" style="left:492px;width:220px;background:var(--blue-light)"></div>
  <div class="block band-top" style="left:712px;width:28px;background:var(--brown-mid)"></div>
  <div class="block band-bottom" style="left:0;width:272px;background:var(--brown-mid)"></div>
  <div class="block band-bottom" style="left:280px;width:212px;background:linear-gradient(90deg,var(--brown-light),var(--brown-dark))"></div>
  <div class="block band-bottom" style="left:492px;width:220px;background:var(--blue-light)"></div>
  <div class="block band-bottom" style="left:712px;width:28px;background:var(--brown-mid)"></div>

  <div class="block portrait" role="img" aria-label="Sepia portrait of a woman in a dark dress with a lace collar"></div>
  <div class="block portrait-edge"></div>
  <h2 class="history-title"><div class="big">The Hartwell<br>Homestead<br>History c.<br>1826</div><div class="place">Alder Falls,<br>New Hampshire</div></h2>
  <div class="story story--left">
    <p>In 1826, George S. Hartwell and his wife, Jane (Pruett) Hartwell purchased 26 acres from Robert Ashby on the Millbrook River, north of Pellham’s Woolen Mill in South Alder Falls, NH. This parcel was carved out lot #32 which was comprised of 268 acres that were deeded to John Ashby (Robert Ashby’s grandfather) by Jeremiah Colby and John Platt on May 5, 1762. It is believed that Hartwell, who was blacksmith, built the house that currently stands at 47 Alder Lane in Alder Falls, NH. He also built his forge on the site down by the river. It is likely that much of the forged hardware in the home was crafted by him. Feeling the need to leave Alder Falls for a new frontier, Hartwell left town with his brother, Asa, to purchase land in the emerging communities of western New York. Before doing so, Hartwell sold the home, shop and buildings to Thomas Larkin and his wife Alice (Mercer) Larkin in 1828.</p>
    <p>By trade, Thomas Larkin was a cloth dresser and wool-carder. He was also a deeply religious man and served as deacon in the emerging, but still quite small, Baptist community. In those days, small groups of the Baptists and Methodists met in the Merriam Home for bible study, prayers and singing. The Merriams were well known abolitionists and their house served as a stop on the Underground Railroad. Deacon Larkin died</p>
  </div>

  <div class="block story-box"></div>
  <div class="story story--middle">
    <p>in 1839 and his estate was managed by Samuel Mercer- very likely a relative of Alice - who protected Alice’s dower. The property was then sold to Elijah Brown Thayer and his wife Achsah (Lund) Thayer.</p>
    <p>Elijah was quite industrious and continued to expand the wool mill. He was an early investor in the Ridgeline Railroad and ceded a right of way to the railroad on the homestead. The mill eventually came under the control of his son, Henry A. Thayer, and operated until it burned down on April 20, 1874. Elijah passed away in 1877 and left the home to Mary Ellen Thayer who was most commonly known as “Ellen.”</p>
    <p>Ellen Thayer was approached in 1891 by Allie Pellham, the owner of the Pellham’s Mill Complex, to ask if she would be willing to rent out the home to a couple from Boston. This turned out to be Lydia and Owen</p>
  </div>
  <div class="block stairs" role="img" aria-label="Photograph of the old wooden staircase and banister"></div>

  <div class="block autumn" role="img" aria-label="Photograph of the yellow farmhouse among autumn trees"></div>
  <div class="block memoir"></div>
  <div class="story story--right">
    <p>Halvorsen, the founders of the Halvorsen Colony, who ended up spending their first summer in Alder Falls, NH in the home. Lydia recalls in her writings: “One cannot forget the two-story farmhouse standing near the iron bridge, where the Dunby Family now lives. It had never known paint and wore a gentle soft gray. Inside were just four rooms and a kitchen, neat as a pin and simply furnished with a few chairs, tables and beds. In the kitchen stood the thing that charmed me most, a stone basin where clear water ran in without pause and then slipped away down a drain....”</p>
    <p>The Dunbys lived in this home for the longest time of any owner--and some refer to this area before the bridge, as Dunbys Corner. This moment of stewardship began under Fred Parker Dunby and his wife Grace E. (Hollis) Dunby around 1904 and lasted until 2015 when a descendant sold the home. The house is now under the stewardship of Edward M. Salvo and Albert A. Pennings, Jr. and will be undergoing a significant restoration.</p>
  </div>
  <div class="block winter" role="img" aria-label="Photograph of the yellow farmhouse in winter snow"></div>
  <div class="block inside-stripe"></div>
</section>

</body>
</html>
```